LedgaVue Business Card

We need a business card design using the attached logo. The company is a financial services company that provides a dashboard (chart based information) for Executives of small businesses to use to better manage their information. The design must be progressive, make good utilization of the logo and project stability and financial security.

Industry/Entity Type

Financial

```html
<!DOCTYPE html>
<html lang="en">
<head>
<meta charset="utf-8">
<title>LedgaVue Business Card</title>
<link rel="stylesheet" href="https://fonts.googleapis.com/css2?family=Questrial&display=swap">
<style>
  :root {
    --stage: #c9b58c;
    --brand-red: #a31b22;
    --ink: #1a1a1a;
    --grey: #8a8a8a;
    --paper: #ffffff;
  }
  * { margin: 0; padding: 0; box-sizing: border-box; }
  html, body { width: 1200px; height: 785px; overflow: hidden; }
  body {
    background: var(--stage);
    font-family: "Questrial", "Century Gothic", sans-serif;
    position: relative;
  }
  .card {
    position: absolute;
    top: 242px;
    width: 525px;
    height: 300px;
    box-shadow: 0 8px 22px rgba(60, 40, 10, 0.25);
    overflow: hidden;
  }
  .card-front { left: 50px; background: var(--brand-red); color: var(--paper); }
  .card-back { left: 625px; background: var(--paper); color: var(--ink); }

  .wordmark {
    position: absolute;
    display: flex;
    align-items: center;
    gap: 10px;
    font-size: 44px;
    line-height: 1;
  }
  .wordmark-square { display: block; width: 34px; height: 34px; }
  .card-front .wordmark { left: 150px; top: 112px; color: var(--paper); }
  .card-front .wordmark-square { background: var(--paper); }
  .card-front .site { position: absolute; left: 190px; top: 176px; font-size: 10px; letter-spacing: 0.2px; }

  .card-back .wordmark { right: 40px; top: 108px; font-size: 38px; color: var(--ink); }
  .card-back .wordmark-square { width: 30px; height: 30px; background: var(--brand-red); }

  .name-tab { position: absolute; left: 0; top: 28px; width: 12px; height: 30px; background: var(--brand-red); }
  .person { position: absolute; left: 28px; top: 30px; }
  .person-name { font-size: 16px; letter-spacing: 0.5px; text-transform: uppercase; }
  .person-name .surname { color: var(--brand-red); }
  .person-title { font-size: 11px; color: var(--grey); font-style: italic; margin-top: 2px; }

  .contacts { position: absolute; left: 22px; top: 140px; list-style: none; font-size: 13px; line-height: 17px; }
  .contacts li { display: flex; align-items: center; gap: 6px; }
  .contacts svg { width: 10px; height: 10px; fill: none; stroke: var(--grey); stroke-width: 1.2; }

  .bands { position: absolute; left: 0; top: 0; width: 525px; height: 300px; }
  .band-dark { fill: var(--ink); }
  .band-red { fill: var(--brand-red); }
  .address { position: absolute; left: 14px; top: 226px; font-size: 12px; color: var(--paper); }
  .card-back .site { position: absolute; right: 24px; top: 256px; font-size: 11px; color: var(--paper); }
</style>
</head>
<body>
  <section class="card card-front" aria-label="Card front">
    <div class="wordmark"><span class="wordmark-square"></span><span class="wordmark-name">LedgaVue</span></div>
    <p class="site">www.ledgavueconsulting.com</p>
  </section>

  <section class="card card-back" aria-label="Card back">
    <svg class="bands" viewBox="0 0 525 300" aria-hidden="true">
      <polygon class="band-dark" points="0,218 335,218 352,252 0,252"/>
      <polygon class="band-red" points="0,252 352,252 358,262 0,262"/>
      <polygon class="band-red" points="348,238 525,238 525,292 372,292"/>
    </svg>
    <span class="name-tab"></span>
    <div class="person">
      <p class="person-name">Dana <span class="surname">Morrow</span></p>
      <p class="person-title">Managing Director</p>
    </div>
    <div class="wordmark"><span class="wordmark-square"></span><span class="wordmark-name">LedgaVue</span></div>
    <ul class="contacts">
      <li><svg viewBox="0 0 10 10"><rect x="2.5" y="0.8" width="5" height="8.4" rx="1"/></svg>512-555-0148</li>
      <li><svg viewBox="0 0 10 10"><rect x="1" y="3.5" width="8" height="5"/><rect x="2.5" y="1" width="5" height="2.5"/></svg>512-555-0193</li>
      <li><svg viewBox="0 0 10 10"><rect x="1" y="2" width="8" height="6"/><polyline points="1,2 5,5.5 9,2"/></svg>d.morrow@ledgavueconsulting.com</li>
    </ul>
    <p class="address">4815 Brenwick Austin, TX 78701</p>
    <p class="site">www.ledgavueconsulting.com</p>
  </section>
</body>
</html>
```